Lumora Business Card Design

hello,
we are looking for a business card design for our Fintech Company. We are credit card processing company that is also expanding in to the crypto market. We will be focusing on crypto processing, with a crypto wallet and crypto exchange. We like the purple in the logo. We want something modern and sophisticated but at the same time simple and trust worthy to work with banks.

Industry/Entity Type

Fintech

Logo Text

Lumora

```html
<!DOCTYPE html>
<html lang="en">
<head>
<meta charset="utf-8">
<title>Lumora Business Card</title>
<link rel="stylesheet" href="https://fonts.googleapis.com/css2?family=Roboto:wght@500;700&display=swap">
<style>
  :root {
    --stage: #4b4b4b;
    --navy: #25365c;
    --purple: #4e3bbf;
    --line-navy: #44527a;
    --line-purple: #5a47c6;
    --card-light: #ffffff;
    --card-edge: #d9e3ee;
  }
  * { margin: 0; padding: 0; box-sizing: border-box; }
  html, body { width: 1200px; height: 800px; overflow: hidden; }
  body {
    background: var(--stage);
    font-family: "Roboto", Arial, sans-serif;
    position: relative;
  }
  .card {
    position: absolute;
    width: 533px;
    height: 329px;
    overflow: hidden;
  }
  .card--front { left: 49px; top: 84px; }
  .card--back {
    left: 625px; top: 335px;
    background: radial-gradient(ellipse at 50% 50%, var(--card-light) 35%, var(--card-edge) 100%);
  }
  .front-texture {
    position: absolute; inset: 0;
    background: radial-gradient(ellipse at 55% 50%, #ffffff 20%, #e8eef4 70%, #dfe7ef 100%);
  }
  .frame-lines { position: absolute; inset: 0; }
  .wordmark {
    position: absolute;
    left: 0; right: 0;
    text-align: center;
    font-weight: 700;
    color: var(--purple);
    letter-spacing: -2px;
    line-height: 1;
  }
  .card--front .wordmark { top: 122px; font-size: 86px; }
  .card--back .wordmark { top: 40px; font-size: 72px; }
  .holder {
    position: absolute; left: 0; right: 0; top: 165px;
    text-align: center;
  }
  .holder__name {
    font-size: 21px; font-weight: 500; color: var(--purple);
    letter-spacing: 0.3px;
  }
  .holder__title {
    margin-top: 3px;
    font-size: 11px; font-weight: 700; color: var(--navy);
  }
  .contact-row {
    position: absolute; left: 0; right: 0; top: 274px;
    display: flex; justify-content: center; align-items: center;
    font-size: 14px; font-weight: 500; color: var(--purple);
  }
  .contact-row__item { padding: 0 32px; }
  .contact-row__divider {
    width: 2px; height: 22px; background: var(--line-navy);
  }
</style>
</head>
<body>
  <section class="card card--front">
    <div class="front-texture" role="img" aria-label="Soft geometric triangle texture in pale blue-grey"></div>
    <svg class="frame-lines" width="533" height="329" viewBox="0 0 533 329">
      <line x1="27" y1="23" x2="244" y2="23" stroke="#44527a" stroke-width="1.5"/>
      <line x1="27" y1="13" x2="27" y2="235" stroke="#44527a" stroke-width="1.5"/>
      <line x1="511" y1="151" x2="511" y2="313" stroke="#5a47c6" stroke-width="1.5"/>
      <line x1="160" y1="309" x2="527" y2="309" stroke="#5a47c6" stroke-width="1.5"/>
    </svg>
    <div class="wordmark">Lumora</div>
  </section>

  <section class="card card--back">
    <div class="wordmark">Lumora</div>
    <div class="holder">
      <p class="holder__name">NAME EXAMPLE</p>
      <p class="holder__title">JOB TITLE</p>
    </div>
    <div class="contact-row">
      <span class="contact-row__item">111 2222 3333</span>
      <span class="contact-row__divider"></span>
      <span class="contact-row__item">email@website.com</span>
      <span class="contact-row__divider"></span>
      <span class="contact-row__item">www.website.com</span>
    </div>
  </section>
</body>
</html>
```